12 Meter Banner-Design Lagerhalle
Zielgruppe
Wir errichten neue Elektroanlagen für Einfamilenhäuser und Wohnungen.
Hallo,
wir möchten auf 12 Meter drei Banner spannen um die unschönen Rohre und Kabel zu verdecken. Jeder der drei Banner soll 400cm breit und 160cm hoch werden.
-Banner 1 links: Motivationsspruch groß, mittig - : Wer immer tut, was er schon kann, bleibt immer das, was er schon ist.
- Banner 2 mitte : Komfortzone ( Grafiken habe ich im Anhang von dem Aufbau der Komfortzone ) Toll wäre ein selbst erstelltes Design passend zum Unternehmen / Farben Schriftart etc.
-Banner 3 rechts: Motivationsspruch : Zusammenkommen ist ein Beginn, zusammenbleiben ist ein Fortschritt, zusammenarbeiten ist ein Erfolg.
- Design nach Vorgabe Druckpilot ( Datasheet) erstellen
Gundsätzlich wäre super, wenn alle 3 Designs/ Banner miteinander harmonieren. Alles andere ist der Kreativität überlassen.
Schriftart: Fira Sans / Montserrat
Wir würden uns über eine Zusammenarbeit freuen.
Beste Grüße

```html
<!DOCTYPE html>
<html lang="de">
<head>
<meta charset="utf-8">
<title>Banner Lagerhalle – Motivationsspruch</title>
<link href="https://fonts.googleapis.com/css2?family=Montserrat:wght@400;600;700&display=swap" rel="stylesheet">
<style>
  :root {
    --page-bg: #f4f4f5;
    --brand-blue: #1c99cf;
    --brand-blue-soft: #34a5d7;
    --text-white: #ffffff;
  }
  html, body {
    margin: 0;
    width: 1200px;
    height: 1200px;
    overflow: hidden;
    background: var(--page-bg);
    font-family: "Montserrat", sans-serif;
  }
  .banner {
    position: absolute;
    left: 40px;
    top: 376px;
    width: 1120px;
    height: 448px;
    background: var(--brand-blue);
    overflow: hidden;
    color: var(--text-white);
  }
  .banner__backdrop {
    position: absolute;
    inset: 0;
  }
  .banner__quote {
    position: absolute;
    left: 0;
    right: 0;
    top: 158px;
    margin: 0;
    text-align: center;
    font-weight: 400;
    font-size: 39px;
    line-height: 46px;
    letter-spacing: 0.2px;
  }
  .brand {
    position: absolute;
    left: 0;
    right: 0;
    top: 318px;
    display: flex;
    flex-direction: column;
    align-items: center;
  }
  .brand__mark {
    width: 42px;
    height: 42px;
    border: 2px solid var(--text-white);
    border-radius: 50%;
    box-sizing: border-box;
    margin-bottom: 8px;
  }
  .brand__name {
    font-weight: 700;
    font-size: 15px;
    letter-spacing: 0.5px;
    line-height: 1;
  }
  .brand__tagline {
    display: flex;
    align-items: center;
    gap: 4px;
    margin-top: 4px;
    font-weight: 700;
    font-size: 6.5px;
    letter-spacing: 1.6px;
  }
  .brand__rule {
    width: 28px;
    height: 1px;
    background: var(--text-white);
  }
</style>
</head>
<body>
  <section class="banner">
    <svg class="banner__backdrop" width="1120" height="448" viewBox="0 0 1120 448" aria-hidden="true">
      <circle cx="275" cy="281" r="160" fill="none" stroke="var(--brand-blue-soft)" stroke-width="16"/>
    </svg>

    <p class="banner__quote">»Wer immer tut, was er schon kann,<br>bleibt immer das, was er schon ist.«</p>

    <div class="brand">
      <div class="brand__mark"></div>
      <div class="brand__name">HALLMANN &amp; REUTER</div>
      <div class="brand__tagline">
        <span class="brand__rule"></span>
        <span>ELEKTROTECHNIK</span>
        <span class="brand__rule"></span>
      </div>
    </div>
  </section>
</body>
</html>
```